Website Design for a High School

School Name: Bayt Qamarin Private Schools
sub-schools:
1-Bayt Qamarin Primary School
2-Bayt Qamarin High School for Girls
3-Bayt Qamarin High School for Boys
The design should be professional and serious and below is the details of the website.
Pages: (Home, About Us, Schools, Events, Students, Gallery, Lectures, Contact Us).
A-) Home Page:
1-Animated photos banner as main
2-Marquee for the last news.
3-Welcoming block of text
4-latest news at the body of the page.
5-Calender "on the side"
6-Number of visitors "on the side"
7-Search bar
8-options to choose a school
B-) School Page:
three schools listed as drop down menu when highlighted over the Schools button in the menu
*Each school page should contain:
1-Student login area
2-Animation photos header
3-Specific news and projects
C-) Student Login page:
have a Report Card
D-) Gallery Page
have a collection of photos.
E-)Contact Page
phone numbers
emails
feedback form
F-)Other mentioned pages
with normal text and photos page look as similar to the Home page.
Required color: Purple as main and include the logo colors
Logo: is attached.
Button link to change language to Arabic.

```html
<!DOCTYPE html>
<html lang="en">
<head>
<meta charset="utf-8">
<title>Bayt Qamarin Private Schools</title>
<link href="https://fonts.googleapis.com/css2?family=Open+Sans:wght@300;400;600&family=Noto+Sans+Arabic:wght@400&display=swap" rel="stylesheet">
<style>
:root{
  --ink:#222222;
  --muted:#777777;
  --line:#d6d6d6;
  --purple:#4a2670;
  --purple-dark:#3a1c5a;
  --accent:#f8c55c;
  --nav-active:#f8c55c;
  --cal-cell:#dcdcdc;
  --cal-today:#7a4fa8;
  --panel:#ececec;
  --white:#ffffff;
}
*{box-sizing:border-box;margin:0;padding:0}
html,body{width:1200px;height:994px;overflow:hidden;background:var(--white)}
body{position:relative;font-family:"Open Sans",Arial,sans-serif;color:var(--ink)}
.abs{position:absolute}

/* header */
.brand-mark{left:210px;top:17px;width:58px;height:58px;border-radius:50%;background:var(--purple)}
.brand-name{left:281px;top:25px;font-size:15.5px;line-height:20px;font-weight:400;letter-spacing:.3px;text-transform:uppercase}
.school-list{left:452px;top:27px;font-size:9px;line-height:15px;list-style:none;color:#333}
.call{left:810px;top:34px;font-size:15px;font-weight:400;color:#444}
.lang{left:932px;top:66px;height:18px;padding:0 10px;border-radius:9px;background:var(--purple);color:var(--white);font-family:"Noto Sans Arabic","Open Sans",sans-serif;font-size:10px;line-height:18px}

/* nav */
.navbar{left:0;top:101px;width:1200px;height:37px;background:var(--purple)}
.nav-links{left:0;top:0;width:760px;height:37px;list-style:none}
.nav-links li{position:absolute;top:0;font-size:12px;line-height:37px;color:var(--white)}
.nav-links li.active{color:var(--nav-active)}
.search{left:777px;top:12px;width:197px;height:15px;border:1px solid #8a6bb0;font-size:8px;color:#b9a6d0;padding:1px 8px;line-height:12px}
.search svg{position:absolute;right:5px;top:2px}

/* banner */
.banner{left:200px;top:149px;width:798px;height:292px;background:linear-gradient(100deg,#e8e3dc 0%,#d9d3cb 35%,#c9bfb3 60%,#8a7766 85%,#6f5a4a 100%)}
.news-bar{left:200px;top:410px;width:798px;height:19px;background:var(--accent);font-size:10px;line-height:19px;text-transform:uppercase}
.news-bar .label{position:absolute;left:24px}
.news-bar .item{position:absolute;left:408px}
.news-bar .item::before{content:"";display:inline-block;width:5px;height:5px;border-radius:50%;background:var(--ink);margin-right:7px;vertical-align:1px}
.arrow{top:265px}

/* welcome */
.welcome{left:200px;top:506px;width:316px;text-align:center}
.welcome-kicker{font-size:9.5px;position:relative;letter-spacing:.2px}
.welcome-kicker::before,.welcome-kicker::after{content:"";position:absolute;top:7px;height:1px;background:var(--line);width:100px}
.welcome-kicker::before{left:0}
.welcome-kicker::after{right:0}
.welcome-title{margin-top:11px;font-size:15px;line-height:20px;font-weight:400;letter-spacing:3.6px;color:var(--muted);text-transform:uppercase}
.welcome-body{left:215px;top:595px;width:295px;font-size:10.2px;line-height:19.9px}
.welcome-body p+p{margin-top:19.9px}
.signature{left:215px;top:793px;font-size:11.5px;line-height:20px}

/* latest news */
.latest{left:531px;top:511px;width:254px;height:304px;background:var(--accent)}
.latest h2{position:absolute;left:34px;top:26px;font-size:15px;font-weight:400;letter-spacing:1.3px}
.latest-photo{position:absolute;left:30px;top:59px;width:81px;height:127px;background:linear-gradient(180deg,#c9a88e 0%,#8a5a45 55%,#7b1f2a 100%)}
.latest-intro{position:absolute;left:122px;top:63px;width:120px;font-size:10px;line-height:19.9px}
.latest-more{position:absolute;left:31px;top:204px;width:210px;font-size:10px;line-height:19.9px}

/* calendar */
.calendar{left:805px;top:512px;width:173px}
.cal-head{height:31px;background:var(--purple-dark);color:var(--white);display:flex;justify-content:space-between;align-items:center;padding:0 8px;font-size:11.5px}
.cal-head .month{font-weight:600}
.cal-head .nav{font-size:7px}
.cal-grid{width:173px;border-collapse:separate;border-spacing:1px;margin-left:-1px}
.cal-grid th{font-size:6px;font-weight:400;height:15px;color:#444;text-transform:uppercase}
.cal-grid td{height:24px;background:var(--cal-cell);text-align:center;font-size:9.5px;color:#333;width:24px}
.cal-grid td.dim{color:#aaa}
.cal-grid td.today{background:var(--cal-today);color:var(--white)}

/* visitors */
.visitors{left:805px;top:693px;width:176px;height:121px;background:var(--panel);text-align:center}
.visitors .label{margin-top:25px;font-size:10px}
.visitors .count{margin-top:13px;font-size:20px;font-weight:300;color:#333}

/* footer */
.footer{left:0;top:892px;width:1200px;border-top:1px solid #eaeaea;text-align:center;font-size:8px;color:#888;padding-top:10px;letter-spacing:.2px}
</style>
</head>
<body>

<header>
  <div class="abs brand-mark"></div>
  <div class="abs brand-name">Bayt Qamarin<br>Private Schools</div>
  <ul class="abs school-list">
    <li>Bayt Qamarin Primary School</li>
    <li>Bayt Qamarin High School for Girls</li>
    <li>Bayt Qamarin High School for Boys</li>
  </ul>
  <div class="abs call">Call us : 1-800-555-0199</div>
  <div class="abs lang" lang="ar">العربية</div>
</header>

<nav class="abs navbar">
  <ul class="abs nav-links">
    <li class="active" style="left:214px">Home</li>
    <li style="left:264px">About Us</li>
    <li style="left:332px">Schools</li>
    <li style="left:388px">Events</li>
    <li style="left:438px">Students</li>
    <li style="left:504px">Gallery</li>
    <li style="left:560px">Lectures</li>
    <li style="left:620px">Contact Us</li>
  </ul>
  <div class="abs search">Type your text here
    <svg width="10" height="10" viewBox="0 0 10 10"><circle cx="4" cy="4" r="3" fill="none" stroke="#d9ccea" stroke-width="1.3"/><line x1="6.2" y1="6.2" x2="9" y2="9" stroke="#d9ccea" stroke-width="1.5"/></svg>
  </div>
</nav>

<section>
  <div class="abs banner" role="img" aria-label="Banner photo of a smiling teacher in front of a classroom of students"></div>
  <div class="abs news-bar">
    <span class="label">Last&nbsp; News</span>
    <span class="item">Bayt Qamarin Private Schools has launched new online courses</span>
  </div>
  <svg class="abs arrow" style="left:161px" width="26" height="53" viewBox="0 0 26 53"><polyline points="25,0 1,26.5 25,53" fill="none" stroke="#111" stroke-width="1.4"/></svg>
  <svg class="abs arrow" style="left:1014px" width="26" height="53" viewBox="0 0 26 53"><polyline points="1,0 25,26.5 1,53" fill="none" stroke="#111" stroke-width="1.4"/></svg>
</section>

<main>
  <div class="abs welcome">
    <div class="welcome-kicker">WELCOME TO</div>
    <h1 class="welcome-title">Bayt Qamarin<br>Private Schools</h1>
  </div>
  <div class="abs welcome-body">
    <p>Lorem ipsum dolor sit amet, consectetur adipisicing elit, sed do eiusmod tempor incididunt ut labore et dolore magna aliqua. Ut enim ad minim veniam, quis nostrud exercitation ullamco laboris nisi ut aliquip ex ea commodo consequat.</p>
    <p>Duis aute irure dolor in reprehenderit in voluptate velit esse cillum dolore eu fugiat nulla pariatur. Excepteur sint occaecat cupidatat non proident, sunt in culpa qui officia deserunt mollit anim id est laborum.</p>
  </div>
  <div class="abs signature">Mr commodo consequat<br>Headmaster</div>

  <article class="abs latest">
    <h2>LATEST NEWS</h2>
    <div class="latest-photo" role="img" aria-label="Photo of a smiling young student in school uniform"></div>
    <p class="latest-intro">Lorem ipsum dolor sit amet, consectetur adipisicing elit, sed do eiusmod tempor incididunt ut labore et dolore magna aliqua.</p>
    <p class="latest-more">Ut enim ad minim veniam, quis nostrud exercitation ullamco laboris nisi ut aliquip ex ea commodo consequat.</p>
  </article>

  <aside class="abs calendar">
    <div class="cal-head"><span class="nav">&#9664;</span><span class="month">March 2011</span><span class="nav">&#9654;</span></div>
    <table class="cal-grid">
      <tr><th>Mon</th><th>Tue</th><th>Wed</th><th>Thu</th><th>Fri</th><th>Sat</th><th>Sun</th></tr>
      <tr><td class="dim">28</td><td>1</td><td>2</td><td>3</td><td class="today">4</td><td>5</td><td>6</td></tr>
      <tr><td>7</td><td>8</td><td>9</td><td>10</td><td>11</td><td>12</td><td>13</td></tr>
      <tr><td>14</td><td>15</td><td>16</td><td>17</td><td>18</td><td>19</td><td>20</td></tr>
      <tr><td>21</td><td>22</td><td>23</td><td>24</td><td>25</td><td>26</td><td>27</td></tr>
      <tr><td>28</td><td>29</td><td>30</td><td>31</td><td class="dim">1</td><td class="dim">2</td><td class="dim">3</td></tr>
    </table>
  </aside>

  <aside class="abs visitors">
    <div class="label">Number of visitors</div>
    <div class="count">4125002</div>
  </aside>
</main>

<footer class="abs footer">Copyright © 2015 Bayt Qamarin Private Schools. Use of this website constitutes acceptance of our User Agreement and Privacy Policy.</footer>

</body>
</html>
```